Flyer Needed to Advertise New Online Reading Programs

ABOUT THE TRUST OF READING DEVELOPMENT
The Trust teaches summer reading skills programs for elementary school students, in programs offered through partnerships with universities, colleges and municipalities nationwide. The goal of each program is to build reading skills, and to foster a lifetime love of books and reading.

AIMS & TARGET MARKET
The Trust has developed a new format of its’ online reading program for elementary students, which includes live small-group video classes taught by a professional reading teacher. The Trust seeks a new graphic design for a flyer to advertise the new online reading program. The flyer will be sent to elementary schools, passed out by teachers, and then taken home by students to show parents; therefore, the primary audience for the flyer will be teachers and parents of elementary school students.

Live classes for children are completely new in online education, unlike anything else in the marketplace, and parents and teachers therefore have no experience with them. The successful design will include illustrations or photographs that allow visitors to immediately grasp/understand the new video class format, without relying heavily on a written description. Additionally, the successful flyer concept will make the program, and the video classes in particular, feel fun and appealing to kids and parents.

Below is additional information about the new live small-group video class format, which meets weekly for 6 weeks:
o During video classes, students participate from home.
o During discussions, the student’s computer (or tablet) screen is filled with live video frames of the teacher and the other students. The video frame for the teacher is larger, and the other students appear in smaller frames.
o During other video class instruction, the teacher uses a presentation screen to display pages of a book or a “whiteboard” used for instructional activities.

Notes: The flyer design could include an illustrated or photo screenshot of a video class, with children looking engaged and a teacher leading them in discussion (stock photos are okay to use in flyer design). We have included a screen shot of one of these classes for reference, but do not feel constrained to represent this screen realistically (as shown here). Layout, look and feel can be changed. Alternatively, you may choose to use a graphic other than a screenshot to bring across the concept of the video classes.

COPY AND SPECIFICATIONS
The flyer design will be one-sided and the dimensions are 8.5” x 11” in either portrait or landscape orientation. We will consider designs in color or black and white. Since we brand our flyers with logos of the universities we partner with throughout the nation, we’ll need to include a partner logo in the design. Exact copy will be provided, but layout is flexible. Screenshots from our sample classes are included to show screen layout. Stock photos are okay to use in flyer designs.

Reason: We'd like to make edits to existing designs.

Hi designers, We wanted to share our thoughts on the main image of the flyer. We're leaning towards an image that shows a sole student on a computer with the computer screen in view. The computer screen could have the sample image we provided to show how the video classes operate. Thanks! The Trust of Reading Development

Graphic Design

```html
<!DOCTYPE html>
<html lang="en">
<head>
<meta charset="utf-8">
<title>Reading Skills Classes Online this Summer – Harbor Grove Education Trust</title>
<link rel="stylesheet" href="https://fonts.googleapis.com/css2?family=Arimo:wght@400;700&display=swap">
<style>
  :root {
    --backdrop: #8a8a8a;
    --paper: #f4f4f4;
    --ink: #3a3a3a;
    --ink-soft: #5c5c5c;
    --ink-muted: #6e6e6e;
    --rule: #9a9a9a;
    --orange: #f07a22;
    --orange-deep: #e4572a;
    --red: #e2283a;
    --photo-warm: #c9a690;
    --photo-cool: #7d8e86;
    --white: #ffffff;
  }
  * { box-sizing: border-box; margin: 0; padding: 0; }
  html, body { width: 1200px; height: 900px; overflow: hidden; }
  body {
    background: var(--backdrop);
    font-family: "Arimo", Arial, sans-serif;
    color: var(--ink);
  }
  .flyer {
    position: absolute;
    left: 270px; top: 23px;
    width: 660px; height: 854px;
    background: var(--paper);
    box-shadow: 0 6px 18px rgba(0,0,0,.25);
    overflow: hidden;
  }
  .hero {
    position: absolute; left: 0; top: 0;
    width: 660px; height: 322px;
  }
  .hero svg { position: absolute; inset: 0; }
  .hero-title {
    position: absolute; right: 30px; top: 70px;
    width: 430px;
    color: var(--white);
    font-size: 24px; font-weight: 400; line-height: 1.25;
    text-align: right;
  }
  .hero-title strong {
    display: inline-block;
    font-weight: 700;
    padding-left: 110px;
    border-top: 1.5px solid var(--white);
    margin-top: 3px;
    padding-top: 2px;
  }
  .perks {
    position: absolute; left: 30px; top: 162px;
    list-style: none;
    color: var(--white);
    font-size: 12.5px; line-height: 1.35;
  }
  .perks li::before { content: "• "; }
  .skills-band {
    position: absolute; left: 0; top: 290px;
    width: 660px; height: 32px;
    display: flex; align-items: center;
    padding-left: 30px;
    color: var(--white);
    font-size: 11.5px;
  }
  .skills-band b { font-weight: 700; font-size: 13px; margin-right: 12px; }
  .programs-title {
    position: absolute; left: 0; top: 352px; width: 660px;
    text-align: center;
    font-size: 14px; font-weight: 700; letter-spacing: .5px;
  }
  .column {
    position: absolute;
    border-left: 1px solid var(--rule);
    padding-left: 12px;
  }
  .column-left { left: 30px; top: 380px; width: 290px; }
  .column-right { left: 345px; top: 410px; width: 290px; }
  .program { margin-bottom: 8px; font-size: 10px; line-height: 1.28; color: var(--ink-soft); }
  .program:last-child { margin-bottom: 0; }
  .program h3 { font-size: 10.5px; font-weight: 700; color: var(--ink); }
  .contact {
    position: absolute; left: 345px; top: 620px;
    width: 290px; height: 110px;
    background: linear-gradient(135deg, var(--orange) 0%, var(--orange-deep) 100%);
    color: var(--white);
    display: flex; align-items: center;
    padding: 0 14px;
  }
  .contact-text { flex: 1; font-size: 11px; line-height: 1.35; text-align: right; padding-right: 14px; border-right: 1px solid rgba(255,255,255,.7); }
  .contact-icon { width: 44px; display: flex; justify-content: center; }
  .partners {
    position: absolute; left: 30px; top: 790px; width: 600px;
    display: flex; align-items: center; justify-content: space-between;
    color: var(--ink-muted);
    font-size: 13px; font-weight: 400;
  }
  .partner { display: flex; align-items: center; gap: 6px; }
  .partner-square { width: 10px; height: 10px; background: var(--ink-muted); }
</style>
</head>
<body>
  <main class="flyer">
    <section class="hero">
      <svg width="660" height="322" viewBox="0 0 660 322">
        <defs>
          <linearGradient id="photoTone" x1="0" y1="0" x2="1" y2="1">
            <stop offset="0" stop-color="#d9b7a3"/>
            <stop offset=".55" stop-color="#c9a690"/>
            <stop offset="1" stop-color="#7d8e86"/>
          </linearGradient>
          <linearGradient id="orangeFade" x1="0" y1="0" x2="1" y2="0">
            <stop offset="0" stop-color="#f07a22" stop-opacity=".95"/>
            <stop offset="1" stop-color="#f39a3a" stop-opacity=".75"/>
          </linearGradient>
        </defs>
        <rect width="660" height="290" fill="url(#photoTone)" role="img" aria-label="Photo of a group of young children gathered around a laptop in a classroom"/>
        <polygon points="0,140 300,140 470,290 0,290" fill="url(#orangeFade)"/>
        <polygon points="200,200 470,290 660,255 660,322 0,322 0,290" fill="#f28a35" fill-opacity=".55"/>
        <rect y="290" width="660" height="32" fill="#e2283a"/>
        <polygon points="380,290 660,245 660,322 480,322" fill="#f28a35" fill-opacity=".55"/>
      </svg>
      <h1 class="hero-title">Reading Skills Classes Online this<br><strong>Summer!</strong></h1>
      <ul class="perks">
        <li>Small class size</li>
        <li>A Skilled &amp; Encouraging Teacher</li>
        <li>Individualized Skills Instruction</li>
        <li>A Program of Independent Reading in Great Books</li>
      </ul>
      <div class="skills-band"><b>READING SKILLS:</b> Phonics Comprehension | Fluency | Study Skills | Speed Reading | Love of Reading</div>
    </section>

    <h2 class="programs-title">PROGRAM DESCRIPTIONS:</h2>

    <div class="column column-left">
      <article class="program">
        <h3>Program for Preschoolers:</h3>
        <p>Students in this program build strong reading readiness skills. Your child will learn letter recognition and beginning phonics, and develop the motivation and love of reading that make learning to read easy, enjoyable and successful.</p>
      </article>
      <article class="program">
        <h3>Program for Entering Kindergartners:</h3>
        <p>Students in this program learn beginning reading skills and develop a love of books. Your child will learn letter recognition, phonics, and sight words, and will learn to sound out short words.</p>
      </article>
      <article class="program">
        <h3>Program for Entering 1st Graders:</h3>
        <p>Students in this program learn to read independently. Your child will learn phonics and sight words, build comprehension, and gain the skills and confidence needed for success in first grade.</p>
      </article>
      <article class="program">
        <h3>Program for Entering 2nd Graders:</h3>
        <p>Students in this program become fluent, independent readers. Your child will make significant gains in phonics and word-attack skills, fluency, and comprehension, and will develop confidence and a love of reading.</p>
      </article>
      <article class="program">
        <h3>Program for Entering 3rd Graders:</h3>
        <p>Students in this program become strong independent readers. Your child will develop the comprehension, fluency, and long-word decoding skills needed to read longer books with ease, and will build confidence and a love of reading.</p>
      </article>
    </div>

    <div class="column column-right">
      <article class="program">
        <h3>Program for Entering 4th and 5th Graders:</h3>
        <p>Students in this program make substantial gains in comprehension, long-word decoding skills, fluency, and reading speed. Your child will complete homework more quickly and easily, be more successful in school, and become a strong, enthusiastic reader.</p>
      </article>
      <article class="program">
        <h3>Programs for Entering 6th-8th Graders and Entering 9th and 10th Graders:</h3>
        <p>Students in these programs make substantial gains in comprehension while doubling reading speed. They also learn the best way to read textbooks, take notes, and study for tests. As a result, students complete homework more quickly and easily, get better grades, and enjoy reading more.</p>
      </article>
    </div>

    <aside class="contact">
      <p class="contact-text">For More Information or to Register<br>Call 1-800-555-0142<br>Mon.–Fri. 8am–6pm, Sat. 9am–3pm<br>and Sun. 10am–2pm<br>Please see reverse side for<br>program schedule.</p>
      <div class="contact-icon">
        <svg width="26" height="40" viewBox="0 0 26 40" aria-label="Phone">
          <path d="M6 2 L12 2 L12 11 L8 13 Q6 20 8 27 L12 29 L12 38 L6 38 Q0 30 0 20 Q0 10 6 2 Z" fill="none" stroke="#fff" stroke-width="2.2" stroke-linejoin="round"/>
        </svg>
      </div>
    </aside>

    <footer class="partners">
      <span class="partner">Lakeside Press</span>
      <span class="partner">BrightPath Education</span>
      <span class="partner"><span class="partner-square"></span>Northfield University</span>
      <span class="partner">Lakeside Press</span>
    </footer>
  </main>
</body>
</html>
```